Etiketten für Imkerei
Zielgruppe
Wir sind eine Imkerei in München. Die Zielgrppe sind Menschen, die lokale Produkte wertschätzen, beim Produzenten gern direkt und auf Märkten einkaufen.
Hallo,
wir benötigen ein universelles Design für Honiggläser-Etiketten, das für verschiedene Sorten verwendet werden kann. Das vorhanden Logo soll im Design aufgenommen werden. Im Logo reicht der Name: Imkerei-Brunntal.

```html
<!DOCTYPE html>
<html lang="de">
<head>
<meta charset="utf-8">
<title>Waldhonig Etiketten – Imkerei Brunntal</title>
<link href="https://fonts.googleapis.com/css2?family=Great+Vibes&family=Quicksand:wght@400;500&display=swap" rel="stylesheet">
<style>
  :root {
    --paper: #fdfbe8;
    --blank: #ffffff;
    --green: #4e6e4f;
    --ink: #2a2a2a;
    --pink: #e0449a;
    --cone: #6f6a55;
    --bee: #5a5545;
  }
  html, body { margin: 0; padding: 0; width: 1200px; height: 960px; overflow: hidden; background: #ffffff; }
  .canvas { position: relative; width: 1500px; height: 1200px; transform: scale(0.8); transform-origin: 0 0; font-family: "Quicksand", sans-serif; color: var(--ink); }
  .shapes { position: absolute; inset: 0; filter: drop-shadow(0 2px 3px rgba(0,0,0,.12)); }
  .vtext { position: absolute; writing-mode: vertical-rl; white-space: nowrap; font-size: 15px; letter-spacing: .3px; }
  .vtext.up { transform: rotate(180deg); }
  .charge { color: var(--pink); font-size: 21px; letter-spacing: 1.5px; }
  .brand { position: absolute; left: 440px; top: 130px; width: 280px; text-align: center; font-size: 30px; font-weight: 500; color: var(--ink); }
  .product { position: absolute; left: 360px; top: 230px; width: 410px; text-align: center; font-family: "Great Vibes", cursive; font-size: 96px; color: var(--green); line-height: 1; }
  .origin { position: absolute; left: 440px; top: 368px; width: 250px; text-align: center; font-size: 23px; letter-spacing: .5px; }
  .weight { position: absolute; left: 490px; top: 474px; width: 150px; text-align: center; font-size: 38px; line-height: 1; }
  .weight small { font-size: 24px; }
  .weight-label { position: absolute; left: 490px; top: 516px; width: 150px; text-align: center; font-size: 13px; }
  .illus { position: absolute; }
</style>
</head>
<body>
<div class="canvas">
  <svg class="shapes" width="1500" height="1200" viewBox="0 0 1500 1200" aria-hidden="true">
    <!-- main wrap label -->
    <rect x="62" y="143" width="1006" height="302" fill="var(--paper)"/>
    <polygon points="270,290 405,38 715,38 850,290 715,542 405,542" fill="var(--paper)"/>
    <polyline points="495,522 428,522 297,290 428,57 693,57 826,290 693,522 636,522" fill="none" stroke="var(--green)" stroke-width="5"/>
    <rect x="72" y="160" width="45" height="270" fill="var(--blank)"/>
    <rect x="160" y="160" width="43" height="135" fill="var(--blank)"/>
    <rect x="1020" y="160" width="8" height="270" fill="var(--blank)"/>
    <line x1="422" y1="350" x2="683" y2="350" stroke="var(--green)" stroke-width="4"/>
    <line x1="392" y1="358" x2="655" y2="358" stroke="var(--green)" stroke-width="2"/>
    <!-- seal one -->
    <polygon points="1178,190 1228,93 1355,93 1405,190 1355,290 1335,290 1335,575 1250,575 1250,290 1228,290" fill="var(--paper)"/>
    <polygon points="1195,190 1240,103 1345,103 1392,190 1345,278 1240,278" fill="none" stroke="var(--green)" stroke-width="4"/>
    <!-- seal two -->
    <polygon points="1178,728 1225,628 1355,628 1400,728 1355,825 1332,825 1332,1105 1248,1105 1248,825 1225,825" fill="var(--paper)"/>
    <polygon points="1193,728 1235,640 1345,640 1388,728 1345,815 1235,815" fill="none" stroke="var(--green)" stroke-width="4"/>
  </svg>

  <!-- left panel -->
  <div class="vtext" style="left:127px; top:162px;">Mindestens haltbar bis Ende:</div>
  <div class="vtext charge" style="left:170px; top:172px;">CHARGE</div>

  <!-- front panel -->
  <div class="brand">Imkerei-Brunntal</div>
  <div class="product">Waldhonig</div>
  <div class="origin">AUS BAYERN</div>
  <div class="illus" role="img" aria-label="Zeichnung eines Tannenzweigs mit Zapfen" style="left:628px; top:408px; width:88px; height:92px; background:radial-gradient(ellipse at 55% 55%, var(--cone) 0%, rgba(111,106,85,.35) 60%, transparent 75%);"></div>
  <div class="weight">500<small>G</small></div>
  <div class="weight-label">Nettogewicht</div>

  <!-- right panel -->
  <div class="vtext up" style="left:955px; top:300px; height:132px;">Imkerei Brunntal</div>
  <div class="vtext up" style="left:975px; top:300px; height:132px;">Lindenweg 7</div>
  <div class="vtext up" style="left:995px; top:240px; height:192px;">80997 München Brunntal</div>
  <div class="vtext up" style="left:1037px; top:160px; height:272px;">Abgefüllt und produziert in Brunntal</div>

  <!-- seal motifs -->
  <div class="illus" role="img" aria-label="Zeichnung einer fliegenden Biene" style="left:1238px; top:148px; width:88px; height:82px; background:radial-gradient(ellipse at 60% 50%, var(--bee) 0%, rgba(90,85,69,.3) 55%, transparent 72%);"></div>
  <div class="illus" role="img" aria-label="Zeichnung eines Tannenzweigs mit Zapfen" style="left:1250px; top:688px; width:86px; height:92px; background:radial-gradient(ellipse at 50% 55%, var(--cone) 0%, rgba(111,106,85,.35) 60%, transparent 75%);"></div>
</div>
</body>
</html>
```